Vértice Solar needs the best stationery in the development business

We need a stationary design for a new company based in Porto, Portugal. We are a new property development management company specialized in downtown regeneration projects and adaptive use of old big textile factories.

We just have selected our new logo in a pixelbazaar competition and now we are searching for the best stationary design. We expect to receive proposals for:

Two sided business cards
A4 main letterhead
A4 simple text papper
A4 and A5 envelops
A4 single folder front page

information for the stationary project

company signature: FormaCrescimentoDireção (as in the logo files attached)

Business card information: 
Tomás Vieira Lobato FRICS
Managing Director

email: tomas@verticesolar-exemplo.pt
website: www.verticesolar-exemplo.pt

adress: 
R. das Camélias, 83 - 2º
4050-217 Porto

office number
+(351) 22 418 76 53
fax number
+(351) 22 418 76 59
mobile
+(351) 934 207 615

Target Market(s)

professional finantial fund managers and big property owners

Industry/Entity Type

Business

Requirements
Must have
• the company logo

Nice to have
• clear simple contemporary design is appreciated

```html
<!DOCTYPE html>
<html lang="pt">
<head>
<meta charset="utf-8">
<title>Vértice Solar — Stationery</title>
<link rel="stylesheet" href="https://fonts.googleapis.com/css2?family=Arimo:wght@400;700&display=swap">
<style>
  :root {
    --backdrop: #6e6e6e;
    --paper: #ffffff;
    --paper-shade: #ececec;
    --brand-blue: #2f62b8;
    --brand-blue-dark: #1f4b9a;
    --ink: #4a4a4a;
    --ink-soft: #8a8a8a;
    --card-black: #141414;
  }
  * { box-sizing: border-box; margin: 0; padding: 0; }
  html, body { width: 1200px; height: 900px; overflow: hidden; }
  body {
    background: var(--backdrop);
    font-family: "Arimo", Arial, sans-serif;
    color: var(--ink);
    position: relative;
  }
  .sheet {
    position: absolute;
    background: var(--paper);
    box-shadow: 3px 3px 0 #d9d9d9, 6px 6px 0 #cfcfcf, 0 4px 14px rgba(0,0,0,.35);
  }
  .brand { display: flex; flex-direction: column; align-items: center; }
  .brand--left { align-items: flex-start; }
  .brand__dot { border-radius: 50%; background: var(--brand-blue); }
  .brand__name { font-weight: 700; color: var(--brand-blue); letter-spacing: -0.5px; white-space: nowrap; line-height: 1; }
  .brand__tag { color: var(--ink-soft); white-space: nowrap; line-height: 1.2; }

  /* A4 folder front */
  .folder-front { left: 97px; top: 45px; width: 358px; height: 462px;
    background: linear-gradient(160deg, #ffffff 0%, #f1f1f1 55%, #e4e4e4 100%); }
  .folder-front .brand { position: absolute; top: 68px; left: 0; right: 0; }
  .folder-front .brand__dot { width: 34px; height: 34px; margin-bottom: 8px; }
  .folder-front .brand__name { font-size: 30px; }
  .folder-front .brand__tag { font-size: 10px; color: var(--brand-blue); }

  /* Letterhead */
  .letterhead { left: 530px; top: 45px; width: 288px; height: 368px; }
  .letterhead__header { height: 50px; background: var(--paper-shade); display: flex; justify-content: space-between; align-items: flex-end; padding: 0 8px 6px 20px; border-right: 5px solid var(--brand-blue); }
  .letterhead .brand__dot { width: 14px; height: 14px; margin-bottom: 3px; }
  .letterhead .brand__name { font-size: 13px; }
  .letterhead__contact { font-size: 5.5px; text-align: right; line-height: 1.5; color: var(--ink); }
  .letterhead__footer { position: absolute; left: 20px; right: 14px; bottom: 8px; border-top: 1px solid var(--brand-blue); padding-top: 4px; display: flex; justify-content: space-between; font-size: 5.5px; }
  .letterhead__edge { position: absolute; left: 0; right: 0; bottom: 0; height: 4px; background: var(--brand-blue); }

  /* Blue folder back */
  .folder-back { left: 845px; top: 45px; width: 293px; height: 378px;
    background: linear-gradient(150deg, #3a70c8 0%, var(--brand-blue) 50%, var(--brand-blue-dark) 100%);
    box-shadow: 3px 3px 0 #2a58a8, 0 4px 14px rgba(0,0,0,.35); }
  .folder-back .brand { position: absolute; top: 140px; left: 0; right: 0; }
  .folder-back .brand__dot { width: 38px; height: 38px; background: #fff; margin-bottom: 8px; }
  .folder-back .brand__name { font-size: 22px; color: #fff; }
  .folder-back .brand__tag { font-size: 7px; color: #dce6f7; }

  /* Envelope */
  .envelope { left: 97px; top: 568px; width: 370px; height: 165px; }
  .envelope .brand { position: absolute; left: 24px; top: 18px; }
  .envelope .brand__dot { width: 18px; height: 18px; margin-bottom: 4px; }
  .envelope .brand__name { font-size: 16px; }
  .envelope__window { position: absolute; left: 26px; top: 108px; width: 130px; height: 31px; border: 1px solid #c8c8c8; border-radius: 3px; background: linear-gradient(#f5f5f5, #e6e6e6); }
  .envelope__address { position: absolute; right: 14px; bottom: 14px; font-size: 6px; text-align: right; line-height: 1.5; }
  .envelope__tab { position: absolute; right: 0; bottom: 14px; width: 5px; height: 18px; background: var(--brand-blue); }

  /* Business card front */
  .card-front { left: 533px; top: 495px; width: 222px; height: 130px;
    background: linear-gradient(160deg, #fff 0%, #eeeeee 100%); }
  .card-front .brand { position: absolute; left: 14px; top: 14px; }
  .card-front .brand__dot { width: 12px; height: 12px; margin-bottom: 2px; }
  .card-front .brand__name { font-size: 11px; }
  .card-front__person { position: absolute; right: 14px; top: 28px; text-align: right; font-size: 6.5px; line-height: 1.4; }
  .card-front__role { color: var(--brand-blue); }
  .card-front__arrow { position: absolute; right: 0; top: 27px; }
  .card-front__details { position: absolute; left: 14px; top: 58px; list-style: none; font-size: 5.5px; line-height: 10px; }
  .card-front__details li { display: flex; align-items: flex-start; gap: 5px; }
  .card-front__details svg { flex: none; margin-top: 2px; }

  /* Business card back */
  .card-back { left: 565px; top: 664px; width: 222px; height: 128px;
    background: radial-gradient(ellipse at 50% 40%, #2e2e2e 0%, var(--card-black) 75%);
    box-shadow: 3px 3px 0 #2a2a2a, 0 4px 14px rgba(0,0,0,.4); }
  .card-back .brand { position: absolute; top: 38px; left: 0; right: 0; }
  .card-back .brand__dot { width: 16px; height: 16px; margin-bottom: 4px; }
  .card-back .brand__name { font-size: 17px; }
  .card-back .brand__tag { font-size: 6px; }
  .card-back__band { position: absolute; left: 0; right: 0; bottom: 6px; height: 11px; background: var(--brand-blue); color: #fff; font-size: 6px; text-align: center; line-height: 11px; letter-spacing: 1px; }

  /* Plain A4 paper */
  .plain-sheet { left: 825px; top: 450px; width: 315px; height: 383px; }
  .plain-sheet .brand { position: absolute; top: 20px; left: 0; right: 0; }
  .plain-sheet .brand__dot { width: 16px; height: 16px; margin-bottom: 4px; }
  .plain-sheet .brand__name { font-size: 15px; }
  .plain-sheet__rule { position: absolute; left: 38px; right: 24px; bottom: 30px; border-top: 1px solid var(--brand-blue); }
  .plain-sheet__tag { position: absolute; left: 0; right: 0; bottom: 15px; text-align: center; font-size: 6px; color: var(--brand-blue); }
  .plain-sheet__edge { position: absolute; left: 0; right: 0; bottom: 0; height: 4px; background: var(--brand-blue); }

  /* Presentation lockup */
  .lockup { position: absolute; left: 115px; top: 752px; }
  .lockup .brand__dot { width: 48px; height: 48px; margin-bottom: 8px; }
  .lockup .brand__name { font-size: 42px; }
  .lockup .brand__tag { font-size: 13px; color: #ffffff; }
</style>
</head>
<body>

<section class="sheet folder-front" aria-label="A4 folder front">
  <div class="brand">
    <span class="brand__dot"></span>
    <span class="brand__name">Vértice Solar</span>
    <span class="brand__tag">FormaCrescimentoDireção</span>
  </div>
</section>

<section class="sheet letterhead" aria-label="A4 letterhead">
  <header class="letterhead__header">
    <div class="brand brand--left">
      <span class="brand__dot"></span>
      <span class="brand__name">Vértice Solar</span>
    </div>
    <address class="letterhead__contact" style="font-style:normal">
      www.verticesolar-exemplo.pt<br>
      tomas@verticesolar-exemplo.pt<br>
      R. das Camélias, 83 - 2º<br>
      4050-217 Porto
    </address>
  </header>
  <footer class="letterhead__footer">
    <span>(o): (351) 22 418 76 53</span>
    <span>(f): (351) 22 418 76 59</span>
    <span>(m): (351) 934 207 615</span>
  </footer>
  <div class="letterhead__edge"></div>
</section>

<section class="sheet folder-back" aria-label="A4 folder back">
  <div class="brand">
    <span class="brand__dot"></span>
    <span class="brand__name">Vértice Solar</span>
    <span class="brand__tag">FormaCrescimentoDireção</span>
  </div>
</section>

<section class="sheet envelope" aria-label="Envelope">
  <div class="brand brand--left">
    <span class="brand__dot"></span>
    <span class="brand__name">Vértice Solar</span>
  </div>
  <div class="envelope__window"></div>
  <address class="envelope__address" style="font-style:normal">
    R. das Camélias, 83 - 2º<br>4050-217 Porto
  </address>
  <div class="envelope__tab"></div>
</section>

<section class="sheet card-front" aria-label="Business card front">
  <div class="brand brand--left">
    <span class="brand__dot"></span>
    <span class="brand__name">Vértice Solar</span>
  </div>
  <div class="card-front__person">
    <div>Tomás Vieira Lobato FRICS</div>
    <div class="card-front__role">Managing Director</div>
  </div>
  <svg class="card-front__arrow" width="6" height="14" viewBox="0 0 6 14"><polygon points="6,0 0,7 6,14" fill="#2f62b8"/></svg>
  <ul class="card-front__details">
    <li><svg width="7" height="6" viewBox="0 0 7 6"><rect x="0" y="2" width="7" height="4" rx="1" fill="#2f62b8"/><rect x="1" y="0" width="5" height="2" rx="1" fill="#2f62b8"/></svg>(351) 22 418 76 53</li>
    <li><svg width="7" height="6" viewBox="0 0 7 6"><path d="M1 0 L2.5 0 L3 2 L2 2.8 Q3 4.5 4.3 4.2 L5 3.4 L7 4 L7 5.5 Q3 6.5 0.5 1.5 Z" fill="#2f62b8"/></svg>(351) 934 207 615</li>
    <li><svg width="7" height="6" viewBox="0 0 7 6"><rect x="0" y="0" width="7" height="6" rx="1" fill="#2f62b8"/><rect x="1.5" y="1" width="4" height="1.5" fill="#fff"/></svg>(351) 22 418 76 59</li>
    <li><svg width="7" height="6" viewBox="0 0 7 6"><rect x="0" y="0.5" width="7" height="5" fill="#2f62b8"/><polyline points="0,0.5 3.5,3.5 7,0.5" fill="none" stroke="#fff" stroke-width="0.8"/></svg>tomas@verticesolar-exemplo.pt</li>
    <li><svg width="7" height="8" viewBox="0 0 7 8"><path d="M3.5 0 A3 3 0 0 1 6.5 3 Q6.5 5 3.5 8 Q0.5 5 0.5 3 A3 3 0 0 1 3.5 0 Z" fill="#2f62b8"/><circle cx="3.5" cy="3" r="1" fill="#fff"/></svg><span>R. das Camélias, 83 - 2º<br>4050-217 Porto</span></li>
  </ul>
</section>

<section class="sheet card-back" aria-label="Business card back">
  <div class="brand">
    <span class="brand__dot"></span>
    <span class="brand__name">Vértice Solar</span>
    <span class="brand__tag">FormaCrescimentoDireção</span>
  </div>
  <div class="card-back__band">www.verticesolar-exemplo.pt</div>
</section>

<section class="sheet plain-sheet" aria-label="A4 plain text paper">
  <div class="brand">
    <span class="brand__dot"></span>
    <span class="brand__name">Vértice Solar</span>
  </div>
  <div class="plain-sheet__rule"></div>
  <div class="plain-sheet__tag">FormaCrescimentoDireção</div>
  <div class="plain-sheet__edge"></div>
</section>

<div class="brand lockup" aria-label="Brand lockup">
  <span class="brand__dot"></span>
  <span class="brand__name">Vértice Solar</span>
  <span class="brand__tag">FormaCrescimentoDireção</span>
</div>

</body>
</html>
```